Velvet Lantern rebranding my business with a new business card

I have my new logo and now I need a refresher on my business cards. I really want something fun and fresh. I like black background or anything to make the color pop.
Logo
Name: Velvet Lantern
Contact Info as stated below:
Mara Pelkin
519-555-0147
Logo
Name: Velvet Lantern
Mara Pelkin
519-555-0147
fb.me/VelvetLanternbyMara
Instagram: @VelvetLanternbyMara

Industry/Entity Type

Business

Contact Information for Business Card

double-sided. Logo on one side. Contact info on the other.

Requirements
Must have
• Logo
• Name: Velvet Lantern
• Contact Info as stated below:
• Mara Pelkin
• 519-555-0147
• fb.me/VelvetLanternbyMara
• fb.me/VelvetLanternbyMara

```html
<!DOCTYPE html>
<html lang="en">
<head>
<meta charset="utf-8">
<title>Velvet Lantern – Business Card</title>
<link href="https://fonts.googleapis.com/css2?family=Germania+One&family=Josefin+Sans:wght@400&display=swap" rel="stylesheet">
<style>
  :root {
    --page: #ffffff;
    --card-dark: #050505;
    --card-light: #ffffff;
    --pink: #ec2a7c;
    --ink: #2a2a2a;
    --edge: #e4e4e4;
  }
  html, body {
    margin: 0;
    width: 1200px;
    height: 1200px;
    overflow: hidden;
    background: var(--page);
  }
  .canvas {
    position: relative;
    width: 1200px;
    height: 1200px;
  }
  .card {
    position: absolute;
    left: 234px;
    width: 704px;
    height: 422px;
    box-sizing: border-box;
  }
  .card--front {
    top: 132px;
    background: var(--card-dark);
  }
  .card--back {
    top: 629px;
    background: var(--card-light);
    border: 1px solid var(--edge);
  }
  .brand-mark {
    position: absolute;
    display: flex;
    flex-direction: column;
    align-items: center;
    justify-content: center;
    gap: 14px;
    font-family: "Germania One", system-ui, sans-serif;
    text-align: center;
    line-height: 1;
  }
  .brand-mark__dot {
    width: 34px;
    height: 34px;
    border-radius: 50%;
  }
  .card--front .brand-mark {
    left: 46px;
    top: 52px;
    width: 312px;
    height: 320px;
    color: var(--pink);
    font-size: 46px;
  }
  .card--front .brand-mark__dot { border: 3px solid var(--pink); box-sizing: border-box; }
  .card--back .brand-mark {
    left: 226px;
    top: 82px;
    width: 250px;
    height: 250px;
    color: var(--pink);
    font-size: 40px;
  }
  .card--back .brand-mark__dot { background: var(--pink); }
  .headline {
    position: absolute;
    left: 286px;
    top: 80px;
    margin: 0;
    font-family: "Germania One", system-ui, sans-serif;
    font-weight: 400;
    font-size: 46px;
    letter-spacing: 2px;
    color: var(--pink);
    text-transform: uppercase;
    white-space: nowrap;
  }
  .contact {
    position: absolute;
    left: 398px;
    top: 228px;
    margin: 0;
    padding: 0;
    list-style: none;
    font-family: "Josefin Sans", system-ui, sans-serif;
    font-size: 14.5px;
    color: var(--pink);
  }
  .contact__item {
    display: flex;
    align-items: center;
    height: 28.5px;
  }
  .contact__icon {
    width: 14px;
    height: 14px;
    margin-right: 11px;
    fill: var(--pink);
    flex: none;
  }
</style>
</head>
<body>
<main class="canvas">
  <section class="card card--front" aria-label="Card front with contact details">
    <div class="brand-mark">
      <span class="brand-mark__dot"></span>
      <span>Velvet<br>Lantern</span>
    </div>
    <h1 class="headline">Velvet Lantern</h1>
    <ul class="contact">
      <li class="contact__item">
        <svg class="contact__icon" viewBox="0 0 14 14" aria-hidden="true"><path d="M7 1 L13 6.5 L11.5 6.5 L11.5 13 L8.5 13 L8.5 9 L5.5 9 L5.5 13 L2.5 13 L2.5 6.5 L1 6.5 Z"/></svg>
        Mara Pelkin
      </li>
      <li class="contact__item">
        <svg class="contact__icon" viewBox="0 0 14 14" aria-hidden="true"><path d="M3 1 L5.2 1 L6.2 4 L4.6 5.2 C5.4 7 7 8.6 8.8 9.4 L10 7.8 L13 8.8 L13 11 C13 12.2 12 13 10.8 13 C5.4 12.6 1.4 8.6 1 3.2 C1 2 1.8 1 3 1 Z"/></svg>
        519-555-0147
      </li>
      <li class="contact__item">
        <svg class="contact__icon" viewBox="0 0 14 14" aria-hidden="true"><circle cx="7" cy="7" r="5.5"/></svg>
        fb.me/VelvetLanternbyMara
      </li>
      <li class="contact__item">
        <svg class="contact__icon" viewBox="0 0 14 14" aria-hidden="true"><rect x="1.5" y="1.5" width="11" height="11" rx="2"/></svg>
        @VelvetLanternbyMara
      </li>
    </ul>
  </section>

  <section class="card card--back" aria-label="Card back with brand name">
    <div class="brand-mark">
      <span class="brand-mark__dot"></span>
      <span>Velvet<br>Lantern</span>
    </div>
  </section>
</main>
</body>
</html>
```